Laser Tattoo Removal Business Cards

We are looking for a professional business card design for a laser tattoo removal business. Ideally looking for a black business card design. The name of the business is Lumen Ink Clearing. We place our cards at local tattoo shops so we ideally are looking for something trendy/edgy to draw both male and female clientele in.

Target Market(s)

Male/Female ages 18-60

Contact Information for Business Card

black background ideally.. hoping to stay within greys, whites and black

Font styles to use
Serif
Sans Serif

Colors
121212
a9a9a9
5c5c5c
f5f5f5
ffffff
7f7f7f
606060
848484
9d9d9d

Requirements
Must have
• Employee Info:
• Marisol Dunmore
• Chief Executive Offer
• m: 919.555.0143
• w: 919.555.0178
• f: 919.555.0192
• mdunmore@lumeninkclearing.com
• Address:
• 4185 Fenwick Pkwy, Suite 210
• Raleigh, NC 27617
• Website:
• www.lumeninkclearing.com
Nice to have
• Myabe business name on back or logo on back and employee info on the front

```html
<!DOCTYPE html>
<html lang="en">
<head>
<meta charset="utf-8">
<title>Lumen Ink Clearing — Business Cards</title>
<link rel="stylesheet" href="https://fonts.googleapis.com/css2?family=Arimo:wght@400;700&display=swap">
<style>
  :root {
    --stage: #262626;
    --card: #121212;
    --ink: #ffffff;
    --ink-soft: #f5f5f5;
    --muted: #a9a9a9;
  }
  * { margin: 0; padding: 0; box-sizing: border-box; }
  html, body {
    width: 1200px; height: 900px; overflow: hidden;
    background: var(--stage);
    font-family: "Arimo", Arial, sans-serif;
    color: var(--ink);
  }
  .stage {
    position: relative; width: 1200px; height: 900px;
  }
  .card {
    position: absolute; left: 310px;
    width: 580px; height: 332px;
    background: var(--card);
    border-radius: 18px;
    box-shadow: 0 14px 40px rgba(0,0,0,.55);
  }
  .card--back { top: 90px; }
  .card--front { top: 472px; }

  .wordmark {
    display: flex; align-items: center; gap: 12px;
    font-weight: 400; text-transform: uppercase;
    letter-spacing: .14em; color: var(--ink);
    white-space: nowrap;
  }
  .wordmark__dot {
    width: 10px; height: 10px; border: 1.5px solid var(--ink);
  }
  .card--back .wordmark {
    position: absolute; left: 0; right: 0; top: 128px;
    justify-content: center; font-size: 30px;
  }
  .card--back .website {
    position: absolute; left: 0; right: 0; top: 228px;
    text-align: center; font-size: 15px; color: var(--ink-soft);
  }

  .card--front .wordmark {
    position: absolute; right: 34px; top: 54px; font-size: 19px;
  }
  .person { position: absolute; left: 40px; top: 104px; }
  .person__name {
    font-size: 22px; font-weight: 700; text-transform: uppercase;
    letter-spacing: .01em;
  }
  .person__title { font-size: 14px; color: var(--ink-soft); margin-top: 3px; }

  .address {
    position: absolute; left: 96px; top: 178px;
    font-size: 15px; line-height: 19px; font-style: normal;
  }
  .contacts {
    position: absolute; left: 96px; top: 228px;
    list-style: none; font-size: 15px; line-height: 19px;
  }
  .contacts li { display: flex; align-items: center; gap: 8px; }
  .contacts svg { width: 13px; height: 13px; fill: var(--ink); flex: none; }
</style>
</head>
<body>
<main class="stage">
  <section class="card card--back" aria-label="Card back">
    <div class="wordmark"><span class="wordmark__dot"></span>Lumen Ink Clearing</div>
    <p class="website">www.lumeninkclearing.com</p>
  </section>

  <section class="card card--front" aria-label="Card front">
    <div class="wordmark"><span class="wordmark__dot"></span>Lumen Ink Clearing</div>

    <div class="person">
      <h1 class="person__name">Marisol Dunmore</h1>
      <p class="person__title">Chief Executive Officer</p>
    </div>

    <address class="address">
      4185 Fenwick Pkwy, Suite 210<br>
      Raleigh, NC 27617
    </address>

    <ul class="contacts">
      <li>
        <svg viewBox="0 0 16 16" aria-label="Mobile"><path d="M4 1h8a1 1 0 0 1 1 1v12a1 1 0 0 1-1 1H4a1 1 0 0 1-1-1V2a1 1 0 0 1 1-1zm1 2v9h6V3zm3 10a.8.8 0 1 0 0 .01z"/></svg>
        919.555.0143
      </li>
      <li>
        <svg viewBox="0 0 16 16" aria-label="Phone"><path d="M3.6 1.5 6 4 4.8 5.8c.9 2.2 2.5 3.8 4.7 4.7L11.3 9.3l2.5 2.4-1.6 2.6C6.5 14 2 9.5 1.8 3.1z"/></svg>
        919.555.0178
      </li>
      <li>
        <svg viewBox="0 0 16 16" aria-label="Fax"><path d="M4 1h8v4H4zM2 6h12a1 1 0 0 1 1 1v5h-3v3H4v-3H1V7a1 1 0 0 1 1-1zm3 5v3h6v-3z"/></svg>
        919.555.0192
      </li>
      <li>
        <svg viewBox="0 0 16 16" aria-label="Email"><path d="M1 3h14v1L8 9 1 4zm0 2.5 7 5 7-5V13H1z"/></svg>
        mdunmore@lumeninkclearing.com
      </li>
    </ul>
  </section>
</main>
</body>
</html>
```